Contemporary new French wine brand needs logo and series of label design

to design a new contemporary logo and series of labels for a new French wine brand. We hope to attract not just current French wine drinkers but new ones who may appreciate a less traditional and more modern style.

Reason: we are wanting to extend the project for a few days more to receive more submissions since we had fewer designs submitted than we were expecting, maybe because of the holidays.

Target Market(s)

people who follow the arts community (eg. music, theatre, visual/video arts, dance) --- all mature ages.

Industry/Entity Type

French Wine

Requirements
Must have
• a clear, memorable treatment for the name BRUMAIS with accompanying logo.
Nice to have
• embossing, matte/gloss refinement, tasteful foil stamping, coated stock for the whites to help the integrity of the paper in and out of ice buckets. A combo of say, three types of fonts; a semi custom font for the brand name Brumais and maybe a script and one other.
Should not have
• not traditional French

```html
<!DOCTYPE html>
<html lang="fr">
<head>
<meta charset="utf-8">
<title>Brumais — Cabernet Sauvignon</title>
<link rel="stylesheet" href="https://fonts.googleapis.com/css2?family=Special+Elite&display=swap">
<style>
  :root {
    --paper: #f3efdc;
    --ink: #1b1916;
    --ghost: #cbc7b7;
    --sky-top: #9ea3b3;
    --sky-mid: #d9cdb4;
    --horizon: #e8b27c;
    --sea-warm: #c99a6a;
    --sea-dark: #3a3634;
  }
  html, body {
    margin: 0;
    padding: 0;
    width: 1200px;
    height: 1073px;
    overflow: hidden;
    background: var(--paper);
  }
  .label {
    position: relative;
    width: 1200px;
    height: 1073px;
    background: var(--paper);
    font-family: "Special Elite", "Courier New", monospace;
    color: var(--ink);
  }
  .brand-name {
    position: absolute;
    top: 118px;
    left: 0;
    width: 1200px;
    margin: 0;
    text-align: center;
    font-size: 104px;
    font-weight: 400;
    letter-spacing: 18px;
    line-height: 1;
    padding-left: 18px;
    box-sizing: border-box;
  }
  .landscape {
    position: absolute;
    top: 340px;
    left: 0;
    width: 1200px;
    height: 377px;
    background: linear-gradient(
      to bottom,
      var(--sky-top) 0%,
      var(--sky-mid) 40%,
      var(--horizon) 64%,
      var(--sea-warm) 72%,
      #a4846a 86%,
      var(--sea-dark) 100%
    );
  }
  .info-line {
    position: absolute;
    margin: 0;
    white-space: nowrap;
    line-height: 1;
  }
  .info-line--main {
    color: var(--ink);
    font-size: 42px;
    letter-spacing: 5px;
    text-shadow: 0.6px 0 0 var(--ink), -0.4px 0 0 var(--ink);
  }
  .info-line--echo {
    color: var(--ghost);
    font-size: 31px;
    letter-spacing: 4px;
  }
  .grape-echo-upper { top: 795px; left: 58px; }
  .grape { top: 830px; left: 94px; }
  .grape-echo-lower { top: 865px; left: 58px; }
  .region-echo-upper { top: 890px; left: 490px; }
  .region { top: 915px; left: 292px; }
  .region-echo-lower { top: 955px; left: 490px; }
</style>
</head>
<body>
  <main class="label">
    <h1 class="brand-name">BRUMAIS</h1>

    <div class="landscape" role="img" aria-label="Painted coastal sunset: dark headland on the left, calm sea reflecting a peach horizon under a grey-blue sky"></div>

    <p class="info-line info-line--echo grape-echo-upper" aria-hidden="true">CREPAGE:CABERNET SAUVIGNON</p>
    <p class="info-line info-line--main grape">crépage:cabernet sauvignon</p>
    <p class="info-line info-line--echo grape-echo-lower" aria-hidden="true">crepage;cabernet sauvignon</p>

    <p class="info-line info-line--echo region-echo-upper" aria-hidden="true">REGION:BORDEAUX</p>
    <p class="info-line info-line--main region">région:bordeaux</p>
    <p class="info-line info-line--echo region-echo-lower" aria-hidden="true">region;bordeaux</p>
  </main>
</body>
</html>
```